Cutting Edge Energy Company PowerPoint Design

Need PowerPoint template for energy company whose primary focus is to extract oil and gas from subsurface reservoirs. Would like design to have a sleek, modern, cutting edge feel. Template will be used to present to Investors. Need to have a PR/Investor relations feel with the ability to present data, economics, graphs, and photos. Needs to incorporate company logo and company stock photos where possible. Design needs to be able to interchange company names Talvane Resources & Brackmoor Resources within the template depending on audience. Company colors can be seen in Logo. Source files can be provided.

```html
<!DOCTYPE html>
<html lang="en">
<head>
<meta charset="utf-8">
<title>Talvane Resources – Investor Presentation Template</title>
<link href="https://fonts.googleapis.com/css2?family=Arimo:wght@400;700&display=swap" rel="stylesheet">
<style>
:root{
  --navy:#0d3b73;
  --navy-deep:#0a2f5c;
  --sky:#1f9be2;
  --steel:#3c6ba8;
  --ink:#1d2733;
  --grey:#7a8290;
  --rule:#d9dde3;
  --page:#f3f4f6;
  --white:#ffffff;
}
*{box-sizing:border-box;margin:0;padding:0}
h1,h2,h3{font-weight:400}
html,body{width:1200px;height:2824px;overflow:hidden;background:var(--page);font-family:"Arimo",Arial,sans-serif;color:var(--ink)}
.canvas{position:relative;width:1200px;height:2824px}
.slide{position:absolute;width:549px;height:309px;background:var(--white);border-bottom:3px solid var(--navy);overflow:hidden;box-shadow:0 1px 3px rgba(0,0,0,.08)}
.col-a{left:39px}.col-b{left:617px}
.r1{top:35px}.r2{top:384px}.r3{top:726px}.r4{top:1069px}.r5{top:1408px}.r6{top:1749px}.r7{top:2103px}.r8{top:2454px}
.abs{position:absolute}
.rule{position:absolute;left:18px;top:13px;width:22px;height:1.5px;background:var(--navy)}
.title{position:absolute;left:18px;top:19px;font-size:13px;font-weight:400;color:var(--navy);letter-spacing:.2px}
.sub{position:absolute;left:18px;top:36px;font-size:5.5px;color:var(--grey);letter-spacing:.3px}
.brand{position:absolute;right:9px;top:20px;font-size:7px;font-weight:700;color:var(--navy);letter-spacing:.2px}
.photo{position:absolute}
.photo-label{position:absolute;inset:0;display:flex;align-items:center;justify-content:center;color:var(--white);font-weight:700;letter-spacing:1px;text-shadow:0 2px 4px rgba(0,0,0,.35)}
.tiny{font-size:5px;line-height:1.6;color:var(--grey)}
.small{font-size:6px;line-height:1.75;color:var(--grey)}
.cover-name{left:26px;top:95px;font-size:25px;color:var(--white);letter-spacing:1.2px}
.cover-tag{left:32px;top:172px;font-size:15px;font-weight:700;color:var(--white)}
.cover-tag2{left:52px;top:197px;font-size:12px;font-weight:700;color:var(--white)}
.agenda-panel{left:0;top:0;width:118px;height:309px;background:var(--navy)}
.agenda-note{left:10px;top:16px;font-size:5px;color:#cfd9e8}
.agenda-title{left:10px;top:146px;font-size:17px;font-weight:700;color:var(--white);letter-spacing:.5px}
.agenda-brand{left:8px;top:288px;font-size:7px;color:var(--white)}
.agenda-list{position:absolute;left:278px;top:58px;width:260px;list-style:none}
.agenda-list li{position:relative;height:34px;display:flex;align-items:center;padding-left:42px;font-size:9px;color:var(--ink);border-bottom:1px solid var(--rule);letter-spacing:.3px}
.agenda-list li::before{content:"";position:absolute;left:0;top:7px;width:20px;height:20px;border-radius:50%;background:var(--navy)}
.agenda-list li::after{content:"";position:absolute;left:7px;top:14px;width:4px;height:4px;border-top:1.2px solid var(--white);border-right:1.2px solid var(--white);transform:rotate(45deg)}
.content-head{left:274px;top:72px;font-size:9px;font-weight:700;color:var(--ink)}
.content-body{left:274px;top:90px;width:240px}
.wordmark{left:40px;top:110px;width:210px;font-size:30px;font-weight:700;line-height:1.1;color:var(--navy)}
.num{position:absolute;font-size:26px;font-weight:700;color:var(--navy)}
.num-head{position:absolute;font-size:7.5px;color:var(--ink)}
.num-body{position:absolute;width:210px}
.feat-icon{position:absolute;left:20px;width:44px;height:44px;border-radius:50%;background:var(--navy);border:2px solid #c9d6e8;box-shadow:0 0 0 2px var(--white) inset}
.feat-head{position:absolute;left:77px;font-size:7.5px;font-weight:700;color:var(--ink)}
.feat-body{position:absolute;left:77px;width:185px}
.bullets{position:absolute;left:278px;top:150px;width:245px;list-style:none}
.bullets li{position:relative;padding-left:18px;margin-bottom:9px;font-size:5.8px;line-height:1.75;color:var(--grey)}
.bullets li::before{content:"";position:absolute;left:0;top:2px;width:6px;height:6px;border-radius:50%;background:var(--navy)}
.chart-card{left:39px;top:59px;width:469px;height:232px;border:1px solid var(--rule)}
.chart-bar{left:0;top:0;width:100%;height:20px;background:var(--navy);color:var(--white);font-size:6px;font-weight:700;display:flex;align-items:center;justify-content:center;letter-spacing:.3px}
.note{position:absolute;left:265px;width:245px;border-left:2px solid var(--ink);padding:5px 0 5px 14px}
.thanks{background:var(--navy)}
.thanks-name{left:40px;top:160px;width:250px;text-align:center;font-size:20px;color:var(--white);letter-spacing:.8px}
.thanks-rule{left:310px;top:85px;width:1px;height:143px;background:rgba(255,255,255,.7)}
.thanks-title{left:354px;top:88px;font-size:23px;font-weight:400;color:var(--white)}
.contact{position:absolute;left:354px;display:flex;align-items:flex-start;gap:9px;font-size:8.5px;color:var(--white);line-height:1.3}
.contact svg{flex:none;margin-top:1px}
.card{position:absolute;top:67px;width:121px;height:177px;border:1px solid #c8ccd3;border-radius:2px;text-align:center}
.avatar{width:52px;height:52px;border-radius:50%;margin:8px auto 0;background:linear-gradient(160deg,#b9a89a,#6e5c52)}
.card-name{margin-top:20px;font-size:7px;font-weight:700;color:var(--ink)}
.card-body{margin:8px 8px 0;font-size:4.6px;line-height:1.75;color:var(--grey)}
</style>
</head>
<body>
<main class="canvas">

<section class="slide col-a r1">
  <div class="photo" style="inset:0;background:linear-gradient(100deg,#2c2c2c 0%,#5d5d5d 45%,#a0a0a0 70%,#4b4b4b 100%)" role="img" aria-label="Black and white photo of an oil pump jack in a field"></div>
  <div class="abs cover-name">TALVANE RESOURCES</div>
  <div class="abs cover-tag">WE ARE AN ENERGY COMPANY</div>
  <div class="abs cover-tag2">FOCUS IS TO EXTRACT OIL &amp; GAS</div>
</section>

<section class="slide col-b r1">
  <div class="abs agenda-panel"></div>
  <div class="abs agenda-note">Add Your Text Here</div>
  <div class="abs agenda-title">AGENDA</div>
  <div class="abs agenda-brand">TALVANE RESOURCES</div>
  <div class="photo" style="left:118px;top:0;width:164px;height:309px;background:linear-gradient(180deg,#4f9ac8 0%,#8cbfd8 55%,#b07a55 80%,#8a5a3c 100%)" role="img" aria-label="Photo of a rusty oil pump jack against blue sky"></div>
  <ul class="agenda-list">
    <li>INTRODUCTION</li><li>ABOUT US</li><li>WELCOME MESSAGE</li><li>OUR SERVICES</li><li>CHART</li><li>CONTACT US</li>
  </ul>
</section>

<section class="slide col-a r2">
  <span class="rule"></span><h2 class="title">YOUR TITLE HERE</h2><p class="sub">SUBTITLE GOES HERE</p><p class="brand">TALVANE RESOURCES</p>
  <div class="photo" style="left:29px;top:72px;width:491px;height:197px;background:linear-gradient(180deg,#5d87b0 0%,#98abbd 35%,#a57a58 55%,#7d5238 100%)" role="img" aria-label="Photo of a drilling rig on a flat desert plain">
    <div class="photo-label" style="font-size:38px">WELCOME</div>
  </div>
</section>

<section class="slide col-b r2">
  <span class="rule"></span><h2 class="title">YOUR TITLE HERE</h2><p class="sub">SUBTITLE GOES HERE</p><p class="brand">TALVANE RESOURCES</p>
</section>

<section class="slide col-a r3">
  <span class="rule"></span><h2 class="title">YOUR TITLE HERE</h2><p class="sub">SUBTITLE GOES HERE</p><p class="brand">TALVANE RESOURCES</p>
  <div class="abs wordmark">Talvane Resources</div>
  <h3 class="abs content-head">Content Here</h3>
  <p class="abs content-body small">Sed ut perspiciatis unde omnis iste natus error sit voluptatem accusantium doloremque laudantium, totam rem aperiam, eaque ipsa quae ab illo inventore veritatis et quasi architecto beatae vitae dicta sunt explicabo. Nemo enim ipsam voluptatem quia voluptas sit aspernatur aut odit aut fugit, sed quia consequuntur magni dolores eos qui ratione voluptatem sequi nesciunt. Neque porro quisquam est, qui dolorem ipsum quia dolor sit amet, consectetur, adipisci velit, sed quia non numquam eius modi tempora incidunt ut labore et dolore magnam aliquam quaerat voluptatem. Ut enim ad minima veniam, quis nostrum exercitationem ullam corporis suscipit laboriosam, nisi ut aliquid ex ea commodi consequatur. Quis autem vel eum iure reprehenderit qui in ea voluptate velit esse. Sed ut perspiciatis unde omnis iste natus error sit voluptatem accusantium doloremque laudantium, totam rem veritatis et quasi architecto beatae vitae.</p>
</section>

<section class="slide col-b r3">
  <span class="rule"></span><h2 class="title">YOUR TITLE HERE</h2><p class="sub">SUBTITLE GOES HERE</p><p class="brand">TALVANE RESOURCES</p>
  <div class="photo" style="left:29px;top:69px;width:491px;height:209px;background:linear-gradient(180deg,#4c8db8 0%,#78aac7 50%,#9a6a4c 85%,#6f4a35 100%)" role="img" aria-label="Photo of an oil pump jack at sunset">
    <div class="photo-label" style="font-size:38px">OUR SERVICES</div>
  </div>
</section>

<section class="slide col-a r4">
  <span class="rule"></span><h2 class="title">YOUR TITLE HERE</h2><p class="sub">SUBTITLE GOES HERE</p><p class="brand">TALVANE RESOURCES</p>
  <div class="photo" style="left:29px;top:66px;width:491px;height:211px;background:linear-gradient(160deg,#2e2622 0%,#4b3d33 50%,#33302e 100%)" role="img" aria-label="Aerial photo of a drilling site with equipment">
    <div class="photo-label" style="font-size:38px">OUR PROCESS</div>
  </div>
</section>

<section class="slide col-b r4">
  <span class="rule"></span><h2 class="title">YOUR TITLE HERE</h2><p class="sub">SUBTITLE GOES HERE</p><p class="brand">TALVANE RESOURCES</p>
  <div class="num" style="left:16px;top:73px">01</div><div class="num-head" style="left:57px;top:78px">Sed ut perspiciatis unde omnis iste natus error</div><p class="num-body tiny" style="left:57px;top:89px">Nemo enim ipsam voluptatem quia voluptas sit aspernatur aut odit aut fugit, sed quia consequuntur magni dolores eos qui ratione voluptatem sequi nesciunt. Neque porro quisquam est, qui dolorem ipsum.</p>
  <div class="num" style="left:16px;top:142px">02</div><div class="num-head" style="left:57px;top:147px">Sed ut perspiciatis unde omnis iste natus error</div><p class="num-body tiny" style="left:57px;top:158px">Nemo enim ipsam voluptatem quia voluptas sit aspernatur aut odit aut fugit, sed quia consequuntur magni dolores eos qui ratione voluptatem sequi nesciunt. Neque porro quisquam est, qui dolorem ipsum.</p>
  <div class="num" style="left:16px;top:214px">03</div><div class="num-head" style="left:57px;top:219px">Sed ut perspiciatis unde omnis iste natus error</div><p class="num-body tiny" style="left:57px;top:230px">Nemo enim ipsam voluptatem quia voluptas sit aspernatur aut odit aut fugit, sed quia consequuntur magni dolores eos qui ratione voluptatem sequi nesciunt. Neque porro quisquam est, qui dolorem ipsum.</p>
  <div class="num" style="left:293px;top:73px">04</div><div class="num-head" style="left:334px;top:78px">Sed ut perspiciatis unde omnis iste natus error</div><p class="num-body tiny" style="left:334px;top:89px">Nemo enim ipsam voluptatem quia voluptas sit aspernatur aut odit aut fugit, sed quia consequuntur magni dolores eos qui ratione voluptatem sequi nesciunt. Neque porro quisquam est, qui dolorem ipsum.</p>
  <div class="num" style="left:293px;top:142px">05</div><div class="num-head" style="left:334px;top:147px">Sed ut perspiciatis unde omnis iste natus error</div><p class="num-body tiny" style="left:334px;top:158px">Nemo enim ipsam voluptatem quia voluptas sit aspernatur aut odit aut fugit, sed quia consequuntur magni dolores eos qui ratione voluptatem sequi nesciunt. Neque porro quisquam est, qui dolorem ipsum.</p>
  <div class="num" style="left:293px;top:214px">06</div><div class="num-head" style="left:334px;top:219px">Sed ut perspiciatis unde omnis iste natus error</div><p class="num-body tiny" style="left:334px;top:230px">Nemo enim ipsam voluptatem quia voluptas sit aspernatur aut odit aut fugit, sed quia consequuntur magni dolores eos qui ratione voluptatem sequi nesciunt. Neque porro quisquam est, qui dolorem ipsum.</p>
</section>

<section class="slide col-a r5">
  <span class="rule"></span><h2 class="title">YOUR TITLE HERE</h2><p class="sub">SUBTITLE GOES HERE</p><p class="brand">TALVANE RESOURCES</p>
  <div class="feat-icon" style="top:73px"></div>
  <svg class="abs" style="left:34px;top:87px" width="16" height="16" viewBox="0 0 16 16"><path d="M3 6h3l5-3v10l-5-3H3z" fill="#fff"/></svg>
  <h3 class="feat-head" style="top:82px">LOREM IPSUM TEXT</h3>
  <p class="feat-body tiny" style="top:94px">Sed ut perspiciatis unde omnis iste natus error sit voluptatem accusantium doloremque laudantium, totam rem aperiam, eaque ipsa quae ab illo inventore veritatis et quasi architecto beatae vitae dicta sunt explicabo.</p>
  <div class="feat-icon" style="top:146px"></div>
  <svg class="abs" style="left:34px;top:160px" width="16" height="16" viewBox="0 0 16 16"><circle cx="6" cy="9" r="3.2" fill="none" stroke="#fff" stroke-width="1.6"/><circle cx="11.5" cy="4.5" r="2" fill="none" stroke="#fff" stroke-width="1.4"/></svg>
  <h3 class="feat-head" style="top:155px">LOREM IPSUM TEXT</h3>
  <p class="feat-body tiny" style="top:167px">Sed ut perspiciatis unde omnis iste natus error sit voluptatem accusantium doloremque laudantium, totam rem aperiam, eaque ipsa quae ab illo inventore veritatis et quasi architecto beatae vitae dicta sunt explicabo.</p>
  <div class="feat-icon" style="top:219px"></div>
  <svg class="abs" style="left:34px;top:233px" width="16" height="16" viewBox="0 0 16 16"><path d="M5 4L1.5 8 5 12M11 4l3.5 4L11 12M9.5 3l-3 10" fill="none" stroke="#fff" stroke-width="1.3"/></svg>
  <h3 class="feat-head" style="top:229px">LOREM IPSUM TEXT</h3>
  <p class="feat-body tiny" style="top:241px">Sed ut perspiciatis unde omnis iste natus error sit voluptatem accusantium doloremque laudantium, totam rem aperiam, eaque ipsa quae ab illo inventore veritatis et quasi architecto beatae vitae dicta sunt explicabo.</p>
  <div class="photo" style="left:287px;top:48px;width:242px;height:235px;background:linear-gradient(180deg,#3f86b8 0%,#6ea7c9 55%,#a06e4f 85%,#7a5038 100%)" role="img" aria-label="Photo of an oil pump jack against blue sky"></div>
</section>

<section class="slide col-b r5">
  <span class="rule"></span><h2 class="title">YOUR TITLE HERE</h2><p class="sub">SUBTITLE GOES HERE</p><p class="brand">TALVANE RESOURCES</p>
  <p class="abs small" style="left:18px;top:77px;width:512px;font-size:5.4px">Sed ut perspiciatis unde omnis iste natus error sit voluptatem accusantium doloremque laudantium, totam rem aperiam, eaque ipsa quae ab illo inventore veritatis et quasi architecto beatae vitae dicta sunt explicabo. Nemo enim ipsam voluptatem quia voluptas sit aspernatur aut odit aut fugit, sed quia consequuntur magni dolores eos qui ratione voluptatem sequi nesciunt. But I must explain to you how all this mistaken idea of denouncing pleasure and praising pain was born and I will give you a complete account of the system, and expound the actual teachings of the great explorer of the truth, the master-builder of human happiness. No one rejects, dislikes, or avoids pleasure itself, because it is pleasure, but because those who do not know how to pursue pleasure rationally encounter consequences that are extremely painful. Nor again is there anyone who loves or pursues or desires to obtain pain of itself, because it is pain, but because occasionally circumstances occur in which take a trivial example, which of us ever undertakes toil and pain can procure him some great pleasure.</p>
  <div class="photo" style="left:0;top:167px;width:549px;height:142px;background:linear-gradient(180deg,#e9edf1 0%,#8c8a86 25%,#6d6258 70%,#8f8478 100%)" role="img" aria-label="Aerial photo of a drilling rig with trucks on a plain"></div>
</section>

<section class="slide col-a r6">
  <span class="rule"></span><h2 class="title">YOUR TITLE HERE</h2><p class="sub">SUBTITLE GOES HERE</p><p class="brand">TALVANE RESOURCES</p>
  <svg class="abs" style="left:0;top:0" width="549" height="309" viewBox="0 0 549 309" role="img" aria-label="Four diamond photo tiles of a drilling site">
    <defs><linearGradient id="site" x1="0" y1="0" x2="1" y2="1"><stop offset="0" stop-color="#4a4038"/><stop offset="1" stop-color="#8a7a66"/></linearGradient></defs>
    <polygon points="139,59 190,110 139,161 88,110" fill="url(#site)"/>
    <polygon points="193,113 244,164 193,215 142,164" fill="url(#site)"/>
    <polygon points="139,167 190,218 139,269 88,218" fill="url(#site)"/>
    <polygon points="85,113 136,164 85,215 34,164" fill="url(#site)"/>
    <rect x="121" y="146" width="36" height="36" fill="#fff"/>
  </svg>
  <div class="abs" style="left:121px;top:160px;width:36px;text-align:center;font-size:5px;font-weight:700;color:var(--navy);line-height:1.3">TALVANE</div>
  <p class="abs small" style="left:278px;top:80px;width:245px;font-size:6px">Lorem ipsum dolor sit amet, consectetur adipiscing elit, sed do eiusmod tempor incididunt ut labore et dolore magna aliqua. Ut enim ad minim veniam, quis nostrud exercitation ullamco laboris nisi ut aliquip ex ea commodo consequat. Duis aute irure dolor in reprehenderit in voluptate velit essea.</p>
  <ul class="bullets">
    <li>Sed ut perspiciatis unde omnis iste natus error sit voluptatem accusa ntium doloremque laudantium.</li>
    <li>Sed ut perspiciatis unde omnis iste natus error sit voluptatem accusa ntium doloremque laudantium.</li>
    <li>Sed ut perspiciatis unde omnis iste natus error sit voluptatem accusa ntium doloremque laudantium.</li>
    <li>Sed ut perspiciatis unde omnis iste natus error sit voluptatem accusa</li>
  </ul>
</section>

<section class="slide col-b r6">
  <span class="rule"></span><h2 class="title">YOUR TITLE HERE</h2><p class="sub">SUBTITLE GOES HERE</p><p class="brand">TALVANE RESOURCES</p>
  <div class="abs chart-card">
    <div class="abs chart-bar">SED UT PERSPICIATIS UNDE OMNIS ISTE NATUS ERROR SIT VOLUPTATEM</div>
  </div>
  <svg class="abs" style="left:0;top:0" width="549" height="309" viewBox="0 0 549 309" font-family="Arimo, Arial, sans-serif">
    <text x="69" y="100" font-size="5.5" fill="#556">13/01/2021 - 20/08/2021</text>
    <rect x="75" y="122" width="4" height="4" fill="#8a93a0"/><text x="86" y="126" font-size="4" fill="#889">1.25</text>
    <g stroke="#e4e7eb" stroke-width=".6">
      <line x1="100" y1="145" x2="505" y2="145"/><line x1="100" y1="167" x2="505" y2="167"/><line x1="100" y1="189" x2="505" y2="189"/><line x1="100" y1="211" x2="505" y2="211"/>
    </g>
    <line x1="100" y1="233" x2="505" y2="233" stroke="#b8bec7" stroke-width=".6"/>
    <g font-size="4" fill="#889" text-anchor="end">
      <text x="95" y="147">1</text><text x="95" y="169">0.75</text><text x="95" y="191">0.5</text><text x="95" y="213">0.25</text><text x="95" y="235">0</text>
    </g>
    <text x="64" y="190" font-size="4.5" fill="#667" transform="rotate(-90 64 190)">Number</text>
    <path d="M156 181 C185 185,200 212,225 206 S270 170,298 167 S345 160,370 164 S420 168,440 173" fill="none" stroke="#0d3b73" stroke-width="1" stroke-dasharray="1.5 1.5"/>
    <g fill="#0d3b73"><circle cx="156" cy="181" r="2.6"/><circle cx="225" cy="206" r="2.6"/><circle cx="298" cy="167" r="2.6"/><circle cx="370" cy="164" r="2.6"/><circle cx="440" cy="173" r="2.6"/></g>
    <g font-size="6" fill="#334" text-anchor="middle">
      <text x="153" y="193">53%</text><text x="225" y="217">51%</text><text x="298" y="178">54%</text><text x="370" y="175">55%</text><text x="440" y="184">54%</text>
    </g>
    <g font-size="3.6" fill="#889" text-anchor="middle">
      <text x="122" y="241">12/27/2020</text><text x="171" y="241">12/28/2020</text><text x="220" y="241">12/29/2020</text><text x="269" y="241">12/30/2020</text><text x="318" y="241">12/31/2020</text><text x="367" y="241">01/01/2021</text><text x="416" y="241">01/02/2021</text><text x="465" y="241">01/03/2021</text>
    </g>
  </svg>
</section>

<section class="slide col-a r7">
  <span class="rule"></span><h2 class="title">YOUR TITLE HERE</h2><p class="sub">SUBTITLE GOES HERE</p><p class="brand">TALVANE RESOURCES</p>
  <svg class="abs" style="left:0;top:0" width="260" height="309" viewBox="0 0 260 309" font-family="Arimo, Arial, sans-serif">
    <ellipse cx="139" cy="258" rx="75" ry="8" fill="#000" opacity=".12"/>
    <path d="M139 70 A88 88 0 0 1 222.7 185.2 L198.9 177.5 A63 63 0 0 0 139 95 Z" fill="#1f9be2"/>
    <path d="M222.7 185.2 A88 88 0 0 1 190.7 229.2 L176 208.8 A63 63 0 0 0 198.9 177.5 Z" fill="#3c6ba8"/>
    <path d="M190.7 229.2 A88 88 0 0 1 139 246 L139 221 A63 63 0 0 0 176 208.8 Z" fill="#1d2733"/>
    <path d="M139 246 A88 88 0 0 1 139 70 L139 95 A63 63 0 0 0 139 221 Z" fill="#0d3b73"/>
    <g font-size="7" font-weight="700" fill="#fff" text-anchor="middle">
      <text x="198" y="116">30%</text><text x="209" y="204">10%</text><text x="170" y="236">10%</text><text x="66" y="160">50%</text>
    </g>
    <text x="139" y="161" font-size="8.5" font-weight="700" fill="#0d3b73" text-anchor="middle">TALVANE</text>
  </svg>
  <p class="note tiny" style="top:43px">Sed ut perspiciatis unde omnis iste natus error sit voluptatem accusant ium doloremque laudantium, totam rem aperiam, eaque ipsa quae ab illo inventore veritatis et quasi archi tecto inventore veritatis et quasi architecto beatae</p>
  <p class="note tiny" style="top:103px">Sed ut perspiciatis unde omnis iste natus error sit voluptatem accusant ium doloremque laudantium, totam rem aperiam, eaque ipsa quae ab illo inventore veritatis et quasi archi tecto inventore veritatis et quasi architecto beatae</p>
  <p class="note tiny" style="top:163px">Sed ut perspiciatis unde omnis iste natus error sit voluptatem accusant ium doloremque laudantium, totam rem aperiam, eaque ipsa quae ab illo inventore veritatis et quasi archi tecto inventore veritatis et quasi architecto beatae</p>
  <p class="note tiny" style="top:223px">Sed ut perspiciatis unde omnis iste natus error sit voluptatem accusant ium doloremque laudantium, totam rem aperiam, eaque ipsa quae ab illo inventore veritatis et quasi archi tecto inventore veritatis et quasi architecto beatae</p>
</section>

<section class="slide thanks col-b r7">
  <div class="abs thanks-name">TALVANE RESOURCES</div>
  <div class="abs thanks-rule"></div>
  <h2 class="abs thanks-title">Thank You</h2>
  <div class="contact" style="top:133px"><svg width="8" height="10" viewBox="0 0 8 10"><path d="M4 0a3.5 3.5 0 0 0-3.5 3.5C.5 6 4 10 4 10s3.5-4 3.5-6.5A3.5 3.5 0 0 0 4 0zm0 5a1.4 1.4 0 1 1 0-2.8A1.4 1.4 0 0 1 4 5z" fill="#fff"/></svg><span>Lorem ipsum dolor sit amet,<br>consectetur</span></div>
  <div class="contact" style="top:166px"><svg width="9" height="9" viewBox="0 0 9 9"><path d="M2 .5l1.5 2-1 1c.5 1.2 1.3 2 2.5 2.5l1-1 2 1.5-1 1.5C3.5 7.8 1.2 5.5.5 2z" fill="#fff"/></svg><span>555-014-2288</span></div>
  <div class="contact" style="top:190px"><svg width="9" height="9" viewBox="0 0 9 9"><circle cx="4.5" cy="4.5" r="4" fill="none" stroke="#fff" stroke-width=".9"/><ellipse cx="4.5" cy="4.5" rx="1.8" ry="4" fill="none" stroke="#fff" stroke-width=".8"/><line x1=".5" y1="4.5" x2="8.5" y2="4.5" stroke="#fff" stroke-width=".8"/></svg><span>www.talvaneresources.com</span></div>
  <div class="contact" style="top:213px"><svg width="9" height="8" viewBox="0 0 9 8"><rect x=".5" y="1" width="8" height="6" fill="#fff"/><path d="M.5 1l4 3 4-3" fill="none" stroke="#0d3b73" stroke-width=".8"/></svg><span>companyname@mailbox.com</span></div>
</section>

<section class="slide col-a r8">
  <span class="rule"></span><h2 class="title">YOUR TITLE HERE</h2><p class="sub">SUBTITLE GOES HERE</p><p class="brand">TALVANE RESOURCES</p>
  <article class="card" style="left:16px"><div class="avatar" role="img" aria-label="Team member portrait photo"></div><h3 class="card-name">AREN VOLE</h3><p class="card-body">Sed ut perspiciatis unde omnis iste natus error sit voluptatem accusantium doloremque laudantium, totam rem aperiam, eaque ipsa quae ab illo inventore veritatis et quasi architecto beatae vitae dicta sunt explicabo. Nemo enim ipsam voluptatem quia voluptas sit aspernatur aut odit aut fugit, sed quia consequuntur magni dolores.</p></article>
  <article class="card" style="left:148px"><div class="avatar" role="img" aria-label="Team member portrait photo"></div><h3 class="card-name">AREN VOLE</h3><p class="card-body">Sed ut perspiciatis unde omnis iste natus error sit voluptatem accusantium doloremque laudantium, totam rem aperiam, eaque ipsa quae ab illo inventore veritatis et quasi architecto beatae vitae dicta sunt explicabo. Nemo enim ipsam voluptatem quia voluptas sit aspernatur aut odit aut fugit, sed quia consequuntur magni dolores.</p></article>
  <article class="card" style="left:280px"><div class="avatar" role="img" aria-label="Team member portrait photo"></div><h3 class="card-name">AREN VOLE</h3><p class="card-body">Sed ut perspiciatis unde omnis iste natus error sit voluptatem accusantium doloremque laudantium, totam rem aperiam, eaque ipsa quae ab illo inventore veritatis et quasi architecto beatae vitae dicta sunt explicabo. Nemo enim ipsam voluptatem quia voluptas sit aspernatur aut odit aut fugit, sed quia consequuntur magni dolores.</p></article>
  <article class="card" style="left:412px"><div class="avatar" role="img" aria-label="Team member portrait photo"></div><h3 class="card-name">AREN VOLE</h3><p class="card-body">Sed ut perspiciatis unde omnis iste natus error sit voluptatem accusantium doloremque laudantium, totam rem aperiam, eaque ipsa quae ab illo inventore veritatis et quasi architecto beatae vitae dicta sunt explicabo. Nemo enim ipsam voluptatem quia voluptas sit aspernatur aut odit aut fugit, sed quia consequuntur magni dolores.</p></article>
</section>

</main>
</body>
</html>
```